Coffee House With Cycling Theme Wants Business Cards

We want to create a business card for a coffee house that has a cycling theme. We expect to use the current logo on one side of the business card and we have been considering adding the words 'COFFEE HOUSE' underneath (see example). For the other side of the business card we want an interesting design with tag-line, address and social media links (the normal business card stuff). See examples provided but we are not fixed on having it exactly as shown, we are very open to great creative ideas. Please note our logo has the initials ‘RM' in orange embedded in the design and this must be retained. However, you can play with the words COFFEE HOUSE as well as use the orange color on the backside of the business card, as you see fit. For an image on the backside of the business card it can be a photo, hand-drawn or whatever but it must visually combine coffee and cycling in some way. The interior of the Coffee House will be reclaimed wood, rustic and have an urban feel to it with cycling artifacts hanging from the walls/ceiling, etc. Finally, it would be beneficial if the business card design elements can be easily used on flyers and other promotional assets. Good luck, we are looking forward to seeing your creative ideas.

Target Market(s)

Coffee lovers and cycling fans

Contact Information for Business Card

See project description.

Colors

Designer to choose colors to be used in the design.

Requirements
Must have
• Must use the current logo provided and combine a coffee and bike theme.
Nice to have
• Orange is used in current logo and could be used as an accent color on the backside of the business card.

```html
<!DOCTYPE html>
<html lang="en">
<head>
<meta charset="utf-8">
<title>RM Coffee House – Business Cards</title>
<link rel="stylesheet" href="https://fonts.googleapis.com/css2?family=Fira+Sans:wght@400;500;600;700&display=swap">
<style>
  :root {
    --orange: #f26a2b;
    --charcoal: #3d3d3d;
    --paper: #ffffff;
    --backdrop: #e9e6e2;
    --font: "Fira Sans", sans-serif;
  }
  * { box-sizing: border-box; margin: 0; padding: 0; }
  html, body { width: 1154px; height: 1200px; overflow: hidden; }
  body { background: var(--backdrop); font-family: var(--font); position: relative; }

  .card {
    position: absolute;
    width: 500px;
    height: 880px;
    background: var(--paper);
    box-shadow: 0 4px 14px rgba(0,0,0,0.18);
    overflow: hidden;
  }

  /* Front */
  .card--front { left: 70px; top: 70px; }
  .stripe { position: absolute; left: 0; width: 100%; }
  .stripe--orange { top: 0; height: 26px; background: var(--orange); }
  .stripe--dark { top: 54px; height: 22px; background: var(--charcoal); }

  .brand-name {
    position: absolute;
    left: 0; right: 0;
    top: 360px;
    text-align: center;
    color: var(--orange);
    font-weight: 600;
    line-height: 1;
  }
  .brand-name__initials { display: block; font-size: 150px; letter-spacing: 4px; }
  .brand-name__words { display: block; font-size: 46px; letter-spacing: 2px; margin-top: 8px; }

  /* Back */
  .card--back { left: 600px; top: 240px; }
  .tagline {
    position: absolute;
    left: 40px; top: 168px;
    font-size: 29px;
    font-weight: 500;
    line-height: 1.2;
    color: var(--charcoal);
  }
  .accent { color: var(--orange); }
  .address {
    position: absolute;
    left: 38px; top: 262px;
    font-size: 20px;
    font-weight: 500;
    color: var(--charcoal);
  }
  .address .dot { color: var(--orange); margin: 0 8px; }

  .cup-art {
    position: absolute;
    left: 70px; top: 400px;
    width: 230px; height: 210px;
    border-radius: 12px;
    background: linear-gradient(160deg, #f7a06e 0%, #5a5a5a 55%, var(--charcoal) 100%);
  }

  .contact {
    position: absolute;
    left: 40px; top: 690px;
    font-size: 21px;
    font-weight: 500;
    color: var(--charcoal);
    line-height: 1.6;
    list-style: none;
  }
  .contact__social { display: flex; align-items: center; gap: 10px; }
  .contact__marker {
    width: 22px; height: 22px;
    border: 2px solid var(--orange);
    border-radius: 50%;
  }

  .ride-strip {
    position: absolute;
    right: 18px; top: 30px;
    width: 84px; height: 830px;
    border-radius: 8px;
    background: linear-gradient(180deg, var(--charcoal) 0%, #6a6a6a 50%, var(--charcoal) 100%);
  }
</style>
</head>
<body>

  <section class="card card--front" aria-label="Card front">
    <div class="stripe stripe--orange"></div>
    <div class="stripe stripe--dark"></div>
    <h1 class="brand-name">
      <span class="brand-name__initials">RM</span>
      <span class="brand-name__words">COFFEE HOUSE</span>
    </h1>
  </section>

  <section class="card card--back" aria-label="Card back">
    <p class="tagline">great coffee with a<br>cycling flavored ambiance<span class="accent">.</span></p>
    <p class="address">45 Roaster Lane<span class="dot">•</span>Millbrook</p>

    <div class="cup-art" role="img" aria-label="Illustration of a steaming coffee cup on a saucer"></div>

    <ul class="contact">
      <li>www<span class="accent">.</span>rmcoffeehouse<span class="accent">.</span>com</li>
      <li>jules<span class="accent">@</span>rmcoffeehouse<span class="accent">.</span>com</li>
      <li class="contact__social"><span class="contact__marker"></span><span><span class="accent">@</span>rmcoffeehouse</span></li>
    </ul>

    <div class="ride-strip" role="img" aria-label="Vertical pattern of bicycles and coffee cups"></div>
  </section>

</body>
</html>
```